Fundraiser Flyer and Email Template

We are looking for a flexible coordinated flyer and email template. The feel of both should be more formal or professional. We are not looking for an overly "political" design that features American flags or other "political" symbols.

We are a political fundraising firm that works with elected officials to set up fundraisers for their campaigns. We send the invites to these events via US Mail and email, so we are looking for a standardized template that will work as both an 8.5 x 11 inch printed flyer, as well as an email template.

The information in the email will be text, but images can be used for formatting.

Some clients have a campaign logo, others do not. The format should be flexible enough to either include the logo, or leave it out. Size also varies.

Any colors in the template should be editable so we can match logos as we get them.

We're open to any format that allows us to edit the format as needed. This would include Photoshop, Microsoft Word, etc.

The text of the invite should include space for:

---------------------------------------
NAME
DISTRICT NUMBER AND OFFICE

DATE OF EVENT
TIME OF EVENT

LOCATION
LOCATION ADDRESS
LOCATION CITY, STATE, ZIP

SUGGESTED CONTRIBUTION LEVELS (Typically 3 levels are provided such as Gold: $1,000, Silver: $500, Bronze: $250)

ADDRESS TO SEND CHECKS TO

RSVP CONTACT INFORMATION

The invite will also need fine-print at the bottom that reads:
"Pennsylvania law allows personal, partnership, and PAC contributions. By law we cannot accept corporate contributions
Paid for by [NAME]"

It Professional

Serif
Sans Serif

• Must have spaces for:
• NAME
• DISTRICT NUMBER AND OFFICE
• DATE OF EVENT
• TIME OF EVENT
• LOCATION
• LOCATION ADDRESS
• LOCATION CITY, STATE, ZIP
• SUGGESTED CONTRIBUTION LEVELS (Typically 3 levels are provided such as Gold: $1,000, Silver: $500, Bronze: $250)
• ADDRESS TO SEND CHECKS TO
• RSVP CONTACT INFORMATION
• The invite will also need fine-print at the bottom that reads:
• "Pennsylvania law allows personal, partnership, and PAC contributions. By law we cannot accept corporate contributions
• Paid for by [NAME]"
• It should not be overly "political".

```html
<!DOCTYPE html>
<html lang="en">
<head>
<meta charset="utf-8">
<title>Fundraising Reception Invitation</title>
<link href="https://fonts.googleapis.com/css2?family=Bowlby+One&family=Oleo+Script:wght@700&family=Open+Sans:wght@400&family=Tinos&display=swap" rel="stylesheet">
<style>
  :root {
    --ink: #000000;
    --band-dark: #4a4a4a;
    --band-mid: #9a9a9a;
    --band-light: #e6e6e6;
    --panel-edge: #a9a9a9;
    --panel-center: #ffffff;
    --brand-ink: #3c3c3c;
    --pattern-dark: #1e1e1e;
    --pattern-light: #6f6f6f;
  }
  html, body {
    margin: 0;
    padding: 0;
    overflow: hidden;
    background: #ffffff;
  }
  .flyer {
    position: relative;
    width: 927px;
    height: 1200px;
    overflow: hidden;
    color: var(--ink);
    background: var(--panel-center);
  }
  .header-band {
    position: absolute;
    left: 0; top: 0;
    width: 927px; height: 190px;
    background: linear-gradient(90deg, var(--band-dark) 0%, var(--band-mid) 35%, var(--band-light) 70%, #c8c8c8 100%);
  }
  .header-pattern {
    position: absolute;
    left: 0; top: 0;
    width: 380px; height: 190px;
    background: linear-gradient(135deg, var(--pattern-dark) 0%, var(--pattern-light) 100%);
    opacity: 0.85;
  }
  .brand-name {
    position: absolute;
    left: 386px; top: 56px;
    width: 520px;
    text-align: center;
    font-family: "Bowlby One", sans-serif;
    font-size: 50px;
    line-height: 60px;
    color: var(--brand-ink);
    letter-spacing: 1px;
    white-space: nowrap;
  }
  .main-panel {
    position: absolute;
    left: 0; top: 190px;
    width: 927px; height: 889px;
    background: radial-gradient(ellipse 60% 75% at 50% 45%, var(--panel-center) 30%, #ededed 65%, var(--panel-edge) 100%);
  }
  .line {
    position: absolute;
    left: 0;
    width: 927px;
    text-align: center;
    white-space: nowrap;
    margin: 0;
    font-weight: normal;
  }
  .script {
    font-family: "Oleo Script", cursive;
    font-weight: 700;
    font-style: italic;
  }
  .display { font-family: "Bowlby One", sans-serif; }
  .body-text { font-family: "Open Sans", sans-serif; }
  .invite-lead { top: 214px; font-size: 24px; line-height: 32px; }
  .host-name { top: 248px; font-size: 64px; line-height: 84px; letter-spacing: 1px; }
  .host-office { top: 348px; font-size: 26px; line-height: 36px; }
  .event-lead { top: 428px; font-size: 23px; line-height: 32px; }
  .event-date { top: 468px; font-size: 28px; line-height: 36px; }
  .event-time { top: 507px; font-size: 24px; line-height: 32px; }
  .venue-label { top: 558px; font-size: 28px; line-height: 36px; }
  .venue-address { top: 593px; font-size: 24px; line-height: 32px; }
  .venue-city { top: 626px; font-size: 24px; line-height: 32px; }
  .levels-title { top: 688px; font-size: 26px; line-height: 36px; }
  .levels {
    position: absolute;
    left: 0; top: 736px;
    width: 927px; height: 120px;
  }
  .level {
    position: absolute;
    width: 110px;
    margin-left: -55px;
    text-align: center;
  }
  .level svg { display: block; margin: 0 auto; }
  .level-amount {
    font-family: "Open Sans", sans-serif;
    font-size: 22px;
    line-height: 30px;
    margin-top: 4px;
  }
  .level-gold { left: 358px; }
  .level-silver { left: 476px; }
  .level-bronze { left: 588px; }
  .checks-lead { top: 863px; font-size: 24px; line-height: 32px; }
  .checks-address { top: 894px; font-size: 22px; line-height: 30px; }
  .rsvp-label { top: 932px; font-size: 23px; line-height: 32px; }
  .rsvp-name { top: 970px; font-size: 24px; line-height: 32px; }
  .rsvp-contact { top: 1002px; font-size: 24px; line-height: 32px; }
  .footer-band {
    position: absolute;
    left: 0; top: 1079px;
    width: 927px; height: 121px;
    background: linear-gradient(90deg, #d9d9d9 0%, #bdbdbd 50%, var(--band-mid) 100%);
  }
  .footer-pattern {
    position: absolute;
    left: 667px; top: 1068px;
    width: 260px; height: 132px;
    background: linear-gradient(135deg, var(--pattern-light) 0%, var(--pattern-dark) 100%);
    opacity: 0.9;
  }
  .fine-print {
    position: absolute;
    left: 0; top: 1100px;
    width: 672px;
    text-align: center;
    font-family: "Tinos", serif;
    font-size: 19px;
    line-height: 28px;
    color: var(--ink);
  }
  .fine-print p { margin: 0; }
</style>
</head>
<body>
<div class="flyer">
  <div class="header-band">
    <div class="header-pattern" role="img" aria-label="Decorative checkered square pattern in black and grey"></div>
    <div class="brand-name">COMPANY NAME</div>
  </div>

  <div class="main-panel"></div>

  <p class="line script invite-lead">Please join</p>
  <h1 class="line display host-name">DANIEL WHITFORD</h1>
  <p class="line display host-office">DISTRICT NUMBER &amp; OFFICE</p>

  <p class="line script event-lead">For Fundraising Reception on</p>
  <p class="line display event-date">23RD FEBRUARY’17</p>
  <p class="line body-text event-time">20:00 HOURS</p>

  <p class="line display venue-label">LOCATION</p>
  <p class="line body-text venue-address">LOCATION ADDRESS</p>
  <p class="line body-text venue-city">LOCATION CITY, STATE, ZIP</p>

  <p class="line display levels-title">SUGGESTED CONTRIBUTION LEVELS</p>

  <svg width="0" height="0" style="position:absolute">
    <defs>
      <linearGradient id="gold-fill" x1="0" y1="0" x2="1" y2="1">
        <stop offset="0" stop-color="#fff2a8"/>
        <stop offset="0.5" stop-color="#e2b22a"/>
        <stop offset="1" stop-color="#8a6010"/>
      </linearGradient>
      <linearGradient id="silver-fill" x1="0" y1="0" x2="1" y2="1">
        <stop offset="0" stop-color="#ffffff"/>
        <stop offset="0.5" stop-color="#b8b8b8"/>
        <stop offset="1" stop-color="#5e5e5e"/>
      </linearGradient>
      <linearGradient id="bronze-fill" x1="0" y1="0" x2="1" y2="1">
        <stop offset="0" stop-color="#f3c7a4"/>
        <stop offset="0.5" stop-color="#b8704a"/>
        <stop offset="1" stop-color="#6a3520"/>
      </linearGradient>
    </defs>
  </svg>

  <div class="levels">
    <div class="level level-gold">
      <svg width="100" height="80" viewBox="0 0 100 95" aria-hidden="true">
        <polygon points="50,2 62,35 97,36 69,57 79,92 50,71 21,92 31,57 3,36 38,35" fill="url(#gold-fill)" stroke="#6b4a0a" stroke-width="1.5"/>
      </svg>
      <div class="level-amount">$1000</div>
    </div>
    <div class="level level-silver">
      <svg width="100" height="80" viewBox="0 0 100 95" aria-hidden="true">
        <polygon points="50,2 62,35 97,36 69,57 79,92 50,71 21,92 31,57 3,36 38,35" fill="url(#silver-fill)" stroke="#444444" stroke-width="1.5"/>
      </svg>
      <div class="level-amount">$500</div>
    </div>
    <div class="level level-bronze">
      <svg width="100" height="80" viewBox="0 0 100 95" aria-hidden="true">
        <polygon points="50,2 62,35 97,36 69,57 79,92 50,71 21,92 31,57 3,36 38,35" fill="url(#bronze-fill)" stroke="#4f2616" stroke-width="1.5"/>
      </svg>
      <div class="level-amount">$250</div>
    </div>
  </div>

  <p class="line script checks-lead">Please send your blessings to</p>
  <p class="line body-text checks-address">218, Alder Lane, 190472</p>
  <p class="line script rsvp-label">RSVP</p>
  <p class="line body-text rsvp-name">Margaret Ellison</p>
  <p class="line body-text rsvp-contact">555,***,0147 | margaret@example.com</p>

  <div class="footer-band"></div>
  <div class="footer-pattern" role="img" aria-label="Decorative checkered square pattern in black and grey"></div>
  <div class="fine-print">
    <p>Pennsylvania law allows personal, partnership, and PAC contributions</p>
    <p>By law we cannot accept corporate contributions</p>
    <p>Paid for by [NAME]</p>
  </div>
</div>
</body>
</html>
```